Business Card Design Project - The Kernel Harbor

Company Name - The Kernel Harbor

We need a unique logo and business cards

We are a team of experienced IT professionals who specialize in providing business value to organizations via the analysis and understanding the challenges of your particular organization. We focus on understanding the challenges first, and execute against your priorities partnering with your highly valued key resources.

Our extensive experience and focus on Agile delivery methodologies help our clients continuously improve and deliver quality solutions. Using this approach we will always deliver the greatest return on your investments.

Target Market(s)

Large organizations IT departments

Industry/Entity Type

Business

Font styles to use
Serif
Sans Serif

Requirements
Should not have
• no pictures

```html
<!DOCTYPE html>
<html lang="en">
<head>
<meta charset="UTF-8">
<title>The Kernel Harbor – Business Cards</title>
<link href="https://fonts.googleapis.com/css2?family=Montserrat:wght@400;600;700&display=swap" rel="stylesheet">
<style>
  :root {
    --page-bg: #e9e7e3;
    --card-bg: #ffffff;
    --ink: #2b2b2b;
    --ink-soft: #3a3a3a;
    --magenta: #c8178c;
    --cyan: #5ec6dc;
    --green: #5fb547;
    --lime: #c2d32e;
    --orange: #e48a1f;
    --red: #e02b2b;
    --card-shadow: 0 10px 28px rgba(0,0,0,0.18);
  }
  * { margin: 0; padding: 0; box-sizing: border-box; }
  html, body {
    width: 1200px;
    height: 784px;
    overflow: hidden;
    background: var(--page-bg);
    font-family: "Montserrat", sans-serif;
    color: var(--ink);
  }
  .canvas {
    position: relative;
    width: 1200px;
    height: 784px;
  }
  .card {
    position: absolute;
    top: 230px;
    width: 530px;
    height: 310px;
    background: var(--card-bg);
    box-shadow: var(--card-shadow);
    overflow: hidden;
  }
  .card--contact { left: 50px; }
  .card--brand { left: 620px; }

  .pattern-area {
    position: absolute;
    top: 0;
    right: 0;
    width: 270px;
    height: 175px;
    background: linear-gradient(120deg, var(--magenta) 0%, var(--orange) 30%, var(--lime) 50%, var(--green) 70%, var(--cyan) 85%, var(--red) 100%);
    opacity: 0.9;
  }

  .person {
    position: absolute;
    left: 30px;
    top: 118px;
  }
  .person__name {
    font-size: 20px;
    font-weight: 700;
    color: var(--ink);
    letter-spacing: 0.2px;
  }
  .person__role {
    font-size: 10px;
    font-weight: 600;
    color: var(--ink-soft);
    margin-top: 2px;
  }

  .contact-list {
    position: absolute;
    left: 30px;
    top: 172px;
    list-style: none;
  }
  .contact-list__item {
    display: flex;
    align-items: flex-start;
    gap: 6px;
    font-size: 12.5px;
    font-weight: 600;
    line-height: 17px;
    color: var(--ink);
  }
  .contact-list__icon {
    width: 13px;
    height: 13px;
    margin-top: 2px;
    flex-shrink: 0;
    fill: var(--ink);
    stroke: var(--ink);
  }

  .brand {
    position: absolute;
    inset: 0;
    display: flex;
    flex-direction: column;
    align-items: center;
    justify-content: center;
    gap: 22px;
  }
  .brand__mark {
    width: 70px;
    height: 70px;
    background: var(--magenta);
  }
  .brand__name {
    font-size: 30px;
    font-weight: 600;
    letter-spacing: 1px;
    text-transform: uppercase;
    color: var(--ink);
  }
</style>
</head>
<body>
<main class="canvas">

  <section class="card card--contact">
    <div class="pattern-area" role="img" aria-label="Colourful mosaic of overlapping magenta, cyan, green, lime, orange and red squares"></div>

    <div class="person">
      <p class="person__name">Dale Marston</p>
      <p class="person__role">Managing Director</p>
    </div>

    <ul class="contact-list">
      <li class="contact-list__item">
        <svg class="contact-list__icon" viewBox="0 0 14 14"><rect x="3.5" y="1" width="7" height="12" rx="1.2" fill="none" stroke-width="1.4"/><rect x="5.5" y="10.3" width="3" height="1.2" stroke="none"/></svg>
        555-201-4470
      </li>
      <li class="contact-list__item">
        <svg class="contact-list__icon" viewBox="0 0 14 14"><path d="M3 1.5l2.3 2.6-1.3 1.6c.8 1.7 2.2 3.1 3.9 3.9l1.6-1.3 2.6 2.3-1.4 1.9C6 12 2 8 1.5 3z" stroke="none"/></svg>
        555-318-2096
      </li>
      <li class="contact-list__item">
        <svg class="contact-list__icon" viewBox="0 0 14 14"><rect x="3" y="1" width="8" height="4" fill="none" stroke-width="1.3"/><rect x="1" y="5" width="12" height="5" rx="1" stroke="none"/><rect x="3.5" y="9" width="7" height="4" fill="#fff" stroke-width="1.2"/></svg>
        555-318-2150
      </li>
      <li class="contact-list__item">
        <svg class="contact-list__icon" viewBox="0 0 14 14"><rect x="1" y="3" width="12" height="8.5" rx="1" fill="none" stroke-width="1.4"/><path d="M1.5 3.5L7 8l5.5-4.5" fill="none" stroke-width="1.4"/></svg>
        info@thekernelharbor.com
      </li>
      <li class="contact-list__item">
        <svg class="contact-list__icon" viewBox="0 0 14 14" fill="none" stroke-width="1.2"><circle cx="7" cy="7" r="5.6" fill="none"/><ellipse cx="7" cy="7" rx="2.4" ry="5.6" fill="none"/><path d="M1.4 7h11.2M2.3 4h9.4M2.3 10h9.4" fill="none"/></svg>
        www.thekernelharbor.com
      </li>
      <li class="contact-list__item">
        <svg class="contact-list__icon" viewBox="0 0 14 14"><path d="M7 1.5L1 7h2v5.5h3V9h2v3.5h3V7h2z" stroke="none"/></svg>
        <span>4820 N. Ridgeline Road,<br>Ashford, CO 80000</span>
      </li>
    </ul>
  </section>

  <section class="card card--brand">
    <div class="brand">
      <div class="brand__mark"></div>
      <p class="brand__name">The Kernel Harbor</p>
    </div>
  </section>

</main>
</body>
</html>
```